Website redesign for fast growing company looking to present a unique image

We're looking to revamp our online image to represent the professional, accomplished company we have become. We want to move beyond a templated look and feel to a custom design - we are eager to have you design a new public face for us! In particular, we need creative ways to display text to stand out. We are reaching top-level, C-suite executives and want to give them the confidence that we have the skills, talent, expertise, and knowledge to help their companies grow.

Target Market(s)

contact centers, business process outsourcing

Industry/Entity Type

Call Center

Coding

Coded - Design and coding required

Number of Pages Required

4 page

Font styles to use
Sans Serif

Colors

Designer to choose colors to be used in the design.

Requirements
Must have
• Designed for a professional audience - C-suite executives - but that also shows our personality as a company that is nimble, personable, trustworthy, and smart. Must be lively, but not quirky. Professional, but not overly formal. Be bold with choices for imagery - we want to look unique so go beyond traditional "business/corporate" stock photos. Instead use imagery similar to what is on our staging website - korvanta.com/staging. Do not use the "neon" sign. Use colors to match and complement our logo - bright orange and dark blue. Creative text boxes that we can use throughout the site. I have attached pages of our current staging site to display some of the types of imagery that might work. We are looking for "professional with a personality" Note: this design will be transferred into a Wordpress framework.
Nice to have
• We like the animated text features of the Tellbrook.com site - bold colors, great display of text features that break up the page and engage people to continue scrolling.
Should not have
• Cheesy stock photos of call center agents wearing headsets. Overly used stock photos of professionals in suits shaking hands, high-rise buildings, connection/network graphics. Current management does not like the neon sign graphics displayed on our staging site (korvanta.com/staging). We do not like style of sites that use cartoon-like icons and figures.

```html
<!DOCTYPE html>
<html lang="en">
<head>
<meta charset="utf-8">
<title>Korvanta — Contact Center Experts</title>
<link rel="stylesheet" href="https://fonts.googleapis.com/css2?family=Oswald:wght@400;500&family=Lato:wght@400;700&family=Montserrat:wght@400;500;600&family=Baloo+2:wght@600&display=swap">
<style>
:root{
  --orange:#f26a3c;
  --orange-soft:#f7a183;
  --navy:#264a6e;
  --ink:#2b2b2b;
  --muted:#8a8a8a;
  --grey-bg:#f7f7f7;
  --white:#ffffff;
}
*{margin:0;padding:0;box-sizing:border-box}
html,body{width:1200px;height:4313px;overflow:hidden}
body{position:relative;background:var(--white);font-family:'Lato',sans-serif;color:var(--ink)}
.abs{position:absolute}
.section{position:absolute;left:0;width:1200px}
.heading{font-family:'Oswald',sans-serif;font-weight:400;color:var(--ink);text-align:center;position:absolute;left:0;width:1200px;letter-spacing:-.3px}
.sub{font-family:'Lato',sans-serif;color:var(--muted);font-size:13px;text-align:center;position:absolute;left:0;width:1200px}

/* hero */
.hero{top:0;height:675px;background:linear-gradient(120deg,#5a5048 0%,#8c7b6a 35%,#a89c8e 60%,#4e4a46 100%)}
.brand{position:absolute;left:160px;top:18px;font-family:'Montserrat',sans-serif;font-weight:600;color:var(--orange);font-size:40px;letter-spacing:-1px;line-height:1}
.brand-tag{position:absolute;left:162px;top:64px;font-family:'Montserrat',sans-serif;font-size:8px;letter-spacing:4.5px;color:var(--orange)}
.nav{position:absolute;top:40px;font-family:'Montserrat',sans-serif;font-size:10px;color:var(--white);letter-spacing:.3px}
.nav.active{color:var(--orange)}
.nav-dot{position:absolute;left:540px;top:31px;width:30px;height:30px;border-radius:50%;background:var(--navy);opacity:.85}
.apply{position:absolute;left:934px;top:30px;width:104px;height:37px;background:var(--orange);color:var(--white);font-family:'Oswald',sans-serif;font-size:12px;line-height:37px;text-align:center}
.hero-title{position:absolute;left:338px;top:256px;width:524px;height:117px;background:rgba(242,106,60,.88);color:var(--white);font-family:'Baloo 2',sans-serif;font-weight:600;font-size:42px;line-height:48px;text-align:center;padding-top:11px}
.hero-sub{position:absolute;left:315px;top:397px;width:569px;height:75px;background:rgba(235,235,235,.85);color:#333;font-family:'Montserrat',sans-serif;font-size:17px;line-height:26px;text-align:center;padding-top:11px}

/* orange band */
.band{top:675px;height:254px;background:var(--orange);color:var(--white)}
.band .heading{color:var(--white);font-size:34px;top:50px}
.band p{position:absolute;left:290px;width:620px;top:115px;font-size:12.5px;line-height:26.5px;text-align:center}

/* options ring */
.ring{top:929px;height:608px}
.ring-label{position:absolute;font-family:'Montserrat',sans-serif;font-size:14.5px;color:#444}
.ring-photo{position:absolute;left:432px;top:1121px;width:336px;height:336px;border-radius:50%;background:radial-gradient(circle at 50% 45%,#d9b3a5 0%,#8fa27a 55%,#5f7550 100%)}

/* solutions */
.solutions{top:1537px;height:823px;background:var(--grey-bg)}
.num{position:absolute;top:1768px;font-family:'Oswald',sans-serif;font-size:108px;line-height:1;color:transparent;-webkit-text-stroke:3px var(--navy)}
.num.hot{color:var(--orange)}
.num-label{position:absolute;font-family:'Montserrat',sans-serif;font-size:12.5px;line-height:19px;text-align:center;color:#222;width:110px}
.slide-photo{position:absolute;left:160px;top:1963px;width:615px;height:300px;background:linear-gradient(135deg,#6d6f72 0%,#b9b3ab 45%,#d9d4cc 70%,#9c958d 100%)}
.slide-card{position:absolute;left:678px;top:2002px;width:360px;height:300px;background:var(--navy);color:var(--white);padding:36px 28px 0 40px}
.slide-card h3{font-family:'Montserrat',sans-serif;font-weight:500;font-size:17px;color:var(--orange);margin-bottom:20px}
.slide-card li{list-style:none;position:relative;padding-left:24px;font-size:12px;line-height:21px;margin-bottom:25px}
.slide-card li::before{content:"";position:absolute;left:3px;top:6px;width:7px;height:7px;background:var(--orange);transform:rotate(45deg)}
.dot{position:absolute;top:2279px;width:8px;height:8px;border-radius:50%;background:var(--navy)}
.dot.on{background:none;border:2px solid var(--orange);width:10px;height:10px;top:2278px}

/* benefits */
.benefits-circle{position:absolute;left:261px;top:2512px;width:416px;height:416px;border-radius:50%;background:var(--orange)}
.benefit{position:absolute;left:353px;width:250px;font-size:11.5px;line-height:16px;color:var(--white);z-index:2}
.benefit b{font-weight:700}
.benefit::before{content:"";position:absolute;left:-19px;top:2px;width:11px;height:11px;border-radius:50%;border:2px solid var(--white);box-shadow:inset 0 0 0 2px var(--orange),inset 0 0 0 6px var(--white)}
.benefit-photo{position:absolute;left:640px;top:2494px;width:240px;height:435px;border-radius:45% 45% 30% 30%;background:linear-gradient(180deg,#c79a7c 0%,#f1e6df 35%,#e7e2de 55%,#3e5a86 80%,#2f4b72 100%)}

/* markets */
.market-img{position:absolute;top:3170px;width:203px;height:136px}
.market-label{position:absolute;top:3293px;width:172px;height:55px;background:var(--navy);color:var(--white);font-family:'Montserrat',sans-serif;font-size:12px;line-height:18px;text-align:center;padding-top:9px}
.arrow-btn{position:absolute;top:3392px;width:26px;height:26px;border:1px solid #d8d8d8;background:var(--white)}

/* economics */
.ebook{position:absolute;left:266px;top:3606px;width:188px;height:263px;border:2px solid #4a4a4a;background:linear-gradient(180deg,var(--navy) 0 22%,#ffffff 22% 100%)}
.ebook-copy{position:absolute;left:511px;top:3603px;width:420px;font-size:12.5px;line-height:26.5px;font-style:italic;color:var(--muted)}
.field{position:absolute;left:509px;width:420px;height:44px;border:1px solid #dcdcdc;background:#f5f5f5;font-size:10.5px;color:#777;line-height:42px;padding-left:16px}
.submit{position:absolute;left:509px;top:3832px;width:105px;height:37px;background:var(--navy);color:var(--white);font-family:'Oswald',sans-serif;font-size:12px;line-height:37px;text-align:center}

/* footer */
.footer{top:3951px;height:362px;background:var(--orange);color:var(--white)}
.footer-brand{top:4010px;color:var(--white);font-size:38px}
.footer-tag{top:4053px;color:var(--white)}
.social{position:absolute;top:4081px;width:29px;height:29px;border-radius:50%;background:var(--white)}
.col-head{position:absolute;top:4010px;font-family:'Oswald',sans-serif;font-size:15px;color:var(--white)}
.col-links{position:absolute;top:4047px;font-size:11px;line-height:19.3px;color:#fde3d8}
.copy{position:absolute;left:0;width:1200px;top:4264px;text-align:center;font-size:9.5px;color:#fbc9b6}
</style>
</head>
<body>

<!-- Hero -->
<section class="section hero" role="img" aria-label="Young man working on a laptop at a desk with a coffee mug"></section>
<div class="brand">Korvanta</div>
<div class="brand-tag">CONTACT CENTER EXPERTS</div>
<div class="nav-dot"></div>
<div class="nav active" style="left:553px">HOME</div>
<div class="nav" style="left:613px">MARKETS WE SERVE</div>
<div class="nav" style="left:740px">ABOUT US</div>
<div class="nav" style="left:817px">CONTACT</div>
<svg class="abs" style="left:895px;top:38px" width="18" height="18" viewBox="0 0 18 18" fill="none" stroke="#fff" stroke-width="1.6"><circle cx="7.5" cy="7.5" r="5.5"/><line x1="11.5" y1="11.5" x2="16" y2="16"/></svg>
<div class="apply">APPLY TODAY</div>
<div class="hero-title">Get More from Your<br>Customer Interactions</div>
<div class="hero-sub">Lift Your Top and Bottom Lines with Professional Outsourcing<br>Solutions from Korvanta</div>

<!-- Intro band -->
<section class="section band">
  <h2 class="heading">It’s A New World. Are You Ready?</h2>
  <p>It’s time to find solutions that deliver more value. Shed the manual interactions that cost you money and distract you from your core. Get more by partnering with Korvanta for Customer Service, Tech Support, and Business Process Outsourcing solutions.</p>
</section>

<!-- Options ring -->
<section class="section ring">
  <h2 class="heading" style="top:52px;font-size:34px">Better. Faster. Leaner. Smarter</h2>
  <p class="sub" style="top:119px">Get More from Your Customer Interactions</p>
</section>
<svg class="abs" style="left:400px;top:1089px" width="400" height="400" viewBox="0 0 400 400">
  <circle cx="200" cy="200" r="188" fill="none" stroke="#f7a183" stroke-width="1.5" stroke-dasharray="2 4"/>
  <g fill="#fff" stroke="#f26a3c" stroke-width="2">
    <circle cx="88" cy="49" r="6"/><circle cx="312" cy="49" r="6"/>
    <circle cx="12" cy="200" r="6"/><circle cx="388" cy="200" r="6"/>
    <circle cx="88" cy="350" r="6"/><circle cx="312" cy="350" r="6"/>
  </g>
  <g fill="#f26a3c">
    <circle cx="88" cy="49" r="2.5"/><circle cx="312" cy="49" r="2.5"/>
    <circle cx="12" cy="200" r="2.5"/><circle cx="388" cy="200" r="2.5"/>
    <circle cx="88" cy="350" r="2.5"/><circle cx="312" cy="350" r="2.5"/>
  </g>
</svg>
<div class="ring-photo" role="img" aria-label="Smiling woman on the phone working at a laptop"></div>
<div class="ring-label" style="left:345px;top:1119px">More Options</div>
<div class="ring-label" style="left:752px;top:1123px">More Value</div>
<div class="ring-label" style="left:278px;top:1280px">More Insights</div>
<div class="ring-label" style="left:819px;top:1280px">More Performance</div>
<div class="ring-label" style="left:340px;top:1429px">More Loyalty</div>
<div class="ring-label" style="left:758px;top:1432px">More Focus</div>

<!-- Solutions -->
<section class="section solutions">
  <h2 class="heading" style="top:49px;font-size:35px;line-height:42px">Flexible, versatile, end-to-end outsourcing<br>options to help you get more of what your<br>business needs.</h2>
</section>
<svg class="abs" style="left:0;top:1740px" width="1200" height="170">
  <g fill="none" stroke="#f26a3c" stroke-width="2.5">
    <path d="M255.4 21.6 A70 70 0 1 1 255.4 148.4"/>
    <path d="M474.4 21.6 A70 70 0 1 1 474.4 148.4"/>
    <path d="M693.4 21.6 A70 70 0 1 1 693.4 148.4"/>
    <path d="M916.4 21.6 A70 70 0 1 1 916.4 148.4"/>
  </g>
</svg>
<div class="num" style="left:184px">1</div>
<div class="num" style="left:398px">2</div>
<div class="num hot" style="left:623px">3</div>
<div class="num" style="left:842px">4</div>
<div class="num-label" style="left:230px;top:1796px">Customer<br>Service<br>Contact Center</div>
<div class="num-label" style="left:449px;top:1787px">Tech<br>Support<br>Service<br>Center</div>
<div class="num-label" style="left:668px;top:1796px">Business<br>Process<br>Outsourcing</div>
<div class="num-label" style="left:891px;top:1796px">End-to-<br>End<br>Solutions</div>

<div class="slide-photo" role="img" aria-label="Team of colleagues gathered around a laptop in a bright office"></div>
<div class="slide-card">
  <h3>Business Process Outsourcing</h3>
  <ul>
    <li>Streamline business and back office processes that hold your team back.</li>
    <li>Manage complex transactions with a consistent, processoriented approach.</li>
    <li>Offload manual document processing and data validation tasks.</li>
  </ul>
</div>
<div class="dot" style="left:160px"></div>
<div class="dot on" style="left:174px"></div>
<div class="dot" style="left:192px"></div>
<div class="dot" style="left:206px"></div>

<!-- Benefits -->
<h2 class="heading" style="top:2412px;font-size:35px">Discover the Benets of Outsourcing</h2>
<div class="benefits-circle"></div>
<div class="benefit-photo" role="img" aria-label="Smiling woman sitting cross-legged with a laptop, pointing to the list"></div>
<div class="benefit" style="top:2583px"><b>Shed overhead</b> and invest in core resources.</div>
<div class="benefit" style="top:2613px"><b>Scale up and down</b> as needed.</div>
<div class="benefit" style="top:2643px"><b>Access data</b> to make better business decisions.</div>
<div class="benefit" style="top:2688px"><b>Continuous improvement</b> via performance management.</div>
<div class="benefit" style="top:2733px"><b>Build customer anity</b> with professional service teams.</div>
<div class="benefit" style="top:2778px"><b>Focus on your business</b>, not on labor-intensive processes.</div>
<div class="benefit" style="top:2823px"><b>Reduce risk</b> – Lower headcount, infrastructure, and technology costs.</div>

<!-- Markets -->
<h2 class="heading" style="top:3049px;font-size:35px">We Serve Your Market</h2>
<p class="sub" style="top:3117px">We serve commercial businesses and federal and state government. We can serve you.</p>
<div class="market-img" style="left:160px;background:linear-gradient(135deg,#b46b4d,#e6dcd3 60%,#7a6a62)" role="img" aria-label="Advisor reviewing paperwork with a client"></div>
<div class="market-img" style="left:387px;background:linear-gradient(135deg,#c9b9a3,#efe9e1 55%,#8e7e6c)" role="img" aria-label="Colleagues meeting around a table"></div>
<div class="market-img" style="left:611px;background:linear-gradient(135deg,#a7b6c3,#eef0f2 55%,#7c8a96)" role="img" aria-label="Two women working together at a computer"></div>
<div class="market-img" style="left:835px;background:linear-gradient(135deg,#5b4a3c,#c9a98a 55%,#3f342b)" role="img" aria-label="Smiling woman holding a tablet"></div>
<div class="market-label" style="left:176px">Insurance Contact<br>Center Services</div>
<div class="market-label" style="left:402px">Government Contact<br>Center Solutions</div>
<div class="market-label" style="left:627px">Customer Service for<br>eCommerce</div>
<div class="market-label" style="left:851px">Tech Support contact<br>center solutions</div>
<div class="arrow-btn" style="left:568px"><svg width="24" height="24" viewBox="0 0 24 24"><path d="M14 7l-5 5 5 5" fill="none" stroke="#555" stroke-width="1.5"/></svg></div>
<div class="arrow-btn" style="left:604px"><svg width="24" height="24" viewBox="0 0 24 24"><path d="M10 7l5 5-5 5" fill="none" stroke="#f26a3c" stroke-width="1.5"/></svg></div>

<!-- Economics -->
<h2 class="heading" style="top:3528px;font-size:35px">The Economics of Outsourcing</h2>
<div class="ebook" role="img" aria-label="Cover of the eBook Calculating the Economics of Outsourcing"></div>
<p class="ebook-copy">Take a hard look at your operating model. What overhead and labor costs can you shed? How can you change in order to become more competitive? Our eBook shows you the way.</p>
<div class="field" style="top:3696px">Your Name*</div>
<div class="field" style="top:3765px">Email*</div>
<div class="submit">LINK TO EBOOK</div>

<!-- Footer -->
<footer class="section footer"></footer>
<div class="brand footer-brand">Korvanta</div>
<div class="brand-tag footer-tag">CONTACT CENTER EXPERTS</div>
<div class="social" style="left:161px"></div>
<div class="social" style="left:198px"></div>
<div class="social" style="left:234px"></div>
<div class="social" style="left:273px"></div>
<div class="col-head" style="left:388px">Links</div>
<div class="col-links" style="left:388px">Contact<br>Leadership Team<br>Company Overview<br>Government Services<br>Tech Support Contact Center<br>Customer Service for eCommerce<br>Healthcare &amp; Insurance</div>
<div class="col-head" style="left:613px">Help</div>
<div class="col-links" style="left:613px">Customer Service Contact Center<br>Business Process Outsourcing<br>Tech Support Contact Center<br>Career Opportunities<br>Analytics for Contact Centers<br>Email Us</div>
<div class="col-head" style="left:837px">Location</div>
<div class="col-links" style="left:837px">210 Alder Row Unit 4, Suite 120<br>Fairhaven, ME 04090</div>
<div class="copy">Copyright © KORVANTA CONTACT CENTER EXPERT - 2020 . All Right Reserved.</div>

</body>
</html>
```